La etiqueta deberá contener lo siguiente:
-Titulo: Miel de Agave Kosher
-Logo de VORET (realizado por ustedes, adjunto diseño)
-Logo del certificado: KOSHER (Se adjuntan certificado)
-Mililitros: 750 ml
-Información nutrimental: se adjunta tabla
La miel deberá sobresalir de las demás por el estilo lujoso y llamativo de la etiqueta.

```html
<!DOCTYPE html>
<html lang="es">
<head>
<meta charset="utf-8">
<title>VORET — Miel de Agave Kosher</title>
<link rel="stylesheet" href="https://fonts.googleapis.com/css2?family=Josefin+Sans:wght@300;400;700&family=Arimo:wght@400;700&display=swap">
<style>
  :root {
    --gold-deep: #c8911c;
    --gold-bright: #f6d63d;
    --label-black: #030303;
    --pattern-grey: #1c1c1c;
    --table-text: #c4c4c4;
    --table-line: #bdbdbd;
    --page: #ffffff;
    --ink: #000000;
  }
  html, body {
    margin: 0;
    padding: 0;
    width: 1200px;
    height: 1200px;
    overflow: hidden;
    background: var(--page);
  }
  .artboard { display: block; width: 1200px; height: 1200px; }
  .brand-name { font-family: "Josefin Sans", sans-serif; font-weight: 400; fill: url(#goldVertical); }
  .product-title { font-family: "Josefin Sans", sans-serif; font-weight: 700; fill: url(#goldVertical); letter-spacing: 8px; }
  .net-content { font-family: "Josefin Sans", sans-serif; font-weight: 300; font-size: 14px; fill: #9a9a9a; }
  .importer { font-family: "Josefin Sans", sans-serif; font-weight: 300; font-size: 8px; fill: #8a8a8a; }
  .nutrition-heading { font-family: "Arimo", sans-serif; font-weight: 700; font-size: 16px; fill: #d0d0d0; }
  .nutrition-row { font-family: "Arimo", sans-serif; font-size: 6.4px; fill: var(--table-text); }
  .nutrition-row.strong { font-weight: 700; }
  .care-note { font-family: "Josefin Sans", sans-serif; font-weight: 300; font-size: 6.4px; fill: var(--table-text); }
  .care-note.large { font-size: 7.6px; }
  .batch-label { font-family: "Arimo", sans-serif; font-size: 5.5px; fill: var(--table-text); }
  .seal-caption { font-family: "Arimo", sans-serif; font-size: 32px; fill: var(--ink); }
  .seal-brand { font-family: "Josefin Sans", sans-serif; font-weight: 400; font-size: 16px; fill: url(#goldVertical); letter-spacing: 4px; }
</style>
</head>
<body>
<svg class="artboard" viewBox="0 0 1200 1200" xmlns="http://www.w3.org/2000/svg">
  <defs>
    <linearGradient id="goldBand" x1="0" x2="1" y1="0" y2="0">
      <stop offset="0" stop-color="#c8911c"/>
      <stop offset="0.35" stop-color="#f6d63d"/>
      <stop offset="0.65" stop-color="#f6d63d"/>
      <stop offset="1" stop-color="#c8911c"/>
    </linearGradient>
    <linearGradient id="goldVertical" x1="0" x2="0" y1="0" y2="1">
      <stop offset="0" stop-color="#f6d63d"/>
      <stop offset="1" stop-color="#c8911c"/>
    </linearGradient>
    <radialGradient id="patternTone" cx="0.5" cy="0.5" r="0.7">
      <stop offset="0" stop-color="#0a0a0a"/>
      <stop offset="1" stop-color="#1f1f1f"/>
    </radialGradient>
  </defs>

  <!-- label body -->
  <g class="bottle-label">
    <rect class="gold-band top" x="89" y="386" width="1026" height="12" fill="url(#goldBand)"/>
    <rect class="gold-band bottom" x="89" y="763" width="1026" height="12" fill="url(#goldBand)"/>
    <rect class="label-field" x="89" y="398" width="1026" height="365" fill="url(#patternTone)" role="img" aria-label="Decorative repeating pattern of rounded leaf shapes in dark grey"/>

    <text class="importer" transform="translate(105 412) rotate(90)">Importada por www.voret-miel.mx</text>

    <!-- central hexagon -->
    <polygon class="hex-outer" points="483,376 721,376 838,580 721,784 483,784 366,580" fill="url(#goldBand)"/>
    <polygon class="hex-gap" points="486,381 718,381 832,580 718,779 486,779 372,580" fill="var(--label-black)"/>
    <polygon class="hex-inner" points="488,386 716,386 827,580 716,774 488,774 377,580" fill="none" stroke="url(#goldBand)" stroke-width="2"/>
    <polygon class="hex-fill" points="490,389 714,389 824,580 714,771 490,771 380,580" fill="#070707" role="img" aria-label="Faint honeycomb texture"/>

    <text class="brand-name" x="602" y="506" font-size="30" text-anchor="middle" letter-spacing="6">VORET</text>
    <text class="product-title" x="602" y="591" font-size="34" text-anchor="middle">MIEL DE AGAVE</text>
    <text class="product-title" x="602" y="632" font-size="34" text-anchor="middle">KOSHER</text>

    <circle class="certificate-badge" cx="601" cy="699" r="46" fill="url(#goldVertical)" role="img" aria-label="Kosher certification badge"/>
    <circle cx="601" cy="699" r="36" fill="#1a1408"/>

    <text class="net-content" x="602" y="767" text-anchor="middle">750ml / 1,065g</text>

    <!-- nutrition panel -->
    <g class="nutrition-panel">
      <rect x="948" y="441" width="149" height="188" fill="none" stroke="var(--table-line)" stroke-width="0.8"/>
      <text class="nutrition-heading" x="1022" y="459" text-anchor="middle">Declaración</text>
      <text class="nutrition-heading" x="1022" y="475" text-anchor="middle">Nutrimental</text>

      <text class="nutrition-row strong" x="953" y="496">Contenido energético por envase</text>
      <text class="nutrition-row" x="1092" y="496" text-anchor="end">2,050 kcal</text>
      <text class="nutrition-row" x="1092" y="505" text-anchor="end">8,639 kJ</text>
      <line x1="953" x2="1092" y1="508" y2="508" stroke="var(--table-line)" stroke-width="0.8"/>

      <text class="nutrition-row" x="953" y="516">Tamaño de la porción</text>
      <text class="nutrition-row" x="1092" y="516" text-anchor="end">100g</text>
      <text class="nutrition-row" x="953" y="524">Porciones por envase</text>
      <text class="nutrition-row" x="1092" y="524" text-anchor="end">3.3</text>
      <text class="nutrition-row" x="953" y="533">Contenido energético por porción</text>
      <text class="nutrition-row" x="1092" y="533" text-anchor="end">310 kcal</text>
      <text class="nutrition-row" x="1092" y="541" text-anchor="end">1,309 kJ</text>
      <line x1="953" x2="1092" y1="545" y2="545" stroke="var(--table-line)" stroke-width="1.6"/>

      <text class="nutrition-row" x="953" y="556">Proteínas</text><text class="nutrition-row" x="1092" y="556" text-anchor="end">0 g</text>
      <text class="nutrition-row" x="953" y="564">Grasas</text><text class="nutrition-row" x="1092" y="564" text-anchor="end">0 g</text>
      <text class="nutrition-row" x="969" y="573">Grasa saturada</text><text class="nutrition-row" x="1092" y="573" text-anchor="end">0 g</text>
      <text class="nutrition-row" x="969" y="581">Grasas trans</text><text class="nutrition-row" x="1092" y="581" text-anchor="end">0 mg</text>
      <text class="nutrition-row" x="953" y="590">Hidratos de carbono disponibles</text><text class="nutrition-row" x="1092" y="590" text-anchor="end">77 g</text>
      <text class="nutrition-row" x="969" y="598">Azúcares</text><text class="nutrition-row" x="1092" y="598" text-anchor="end">77 g</text>
      <text class="nutrition-row" x="969" y="607">Azúcares añadidos</text><text class="nutrition-row" x="1092" y="607" text-anchor="end">0 g</text>
      <text class="nutrition-row" x="953" y="615">Fibra dietética</text><text class="nutrition-row" x="1092" y="615" text-anchor="end">menos de 1 g</text>
      <text class="nutrition-row" x="953" y="624">Sodio</text><text class="nutrition-row" x="1092" y="624" text-anchor="end">0 mg</text>
    </g>

    <!-- care icons and notes -->
    <g class="care-icons" fill="none" stroke="var(--table-text)" stroke-width="0.9">
      <circle cx="968" cy="647" r="11"/>
      <rect x="966" y="639" width="4" height="11" rx="2"/>
      <circle cx="968" cy="652" r="3"/>
      <path d="M1019 637 L1030 656 L1008 656 Z"/>
      <line x1="1019" y1="643" x2="1019" y2="650"/>
      <circle cx="1047" cy="647" r="11"/>
      <line x1="1039" y1="655" x2="1055" y2="639"/>
    </g>
    <text class="care-note" x="966" y="666" text-anchor="middle">Store at room</text>
    <text class="care-note" x="966" y="675" text-anchor="middle">temperature</text>
    <text class="care-note" x="1003" y="666">Warning: Honey is not</text>
    <text class="care-note" x="1003" y="675">suitable for children</text>
    <text class="care-note" x="1003" y="684">under 12 months</text>
    <text class="care-note large" x="948" y="700">Raw honey will crystallize. To soften,</text>
    <text class="care-note large" x="948" y="708">place sealed jar in a hot water bath</text>
    <text class="care-note large" x="948" y="716">and heat until desired consistency.</text>

    <rect class="batch-box" x="1076" y="635" width="21" height="59" rx="2" fill="none" stroke="var(--table-line)" stroke-width="0.8"/>
    <text class="batch-label" transform="translate(1087 724) rotate(-90)">BATCH#</text>
  </g>

  <!-- safety seal -->
  <text class="seal-caption" x="422" y="862">Safety seal:</text>
  <g class="safety-seal">
    <polygon points="515,912 737,912 760,954 737,996 515,996" fill="url(#goldBand)"/>
    <polygon points="519,917 734,917 754,954 734,991 519,991" fill="#0a0a0a" role="img" aria-label="Repeating dark leaf pattern"/>
    <circle cx="474" cy="954" r="62" fill="url(#goldVertical)"/>
    <circle cx="474" cy="954" r="55" fill="var(--label-black)"/>
    <text class="seal-brand" transform="translate(492 924) rotate(-90) translate(-62 0)" text-anchor="start">VORET</text>
  </g>
</svg>
</body>
</html>
```